Business Card Design Project - KLB

I am looking for a more sophisticated card design for my company,
"The Kestrel Bureau"

We are a consultancy focused on strategy and change in Associations and professional organisations.

I am a lawyer and psychologist with a PhD and so am looking for something that communicates seriousness and credibility but also quirky creative solutions for strategic problems, which is my field of speciality.

I am looking for something that is quietly spoken, rather than loud colours ('credible' and 'creative' are the two adjectives that I think of as competing here).

I particularly like an embossed card style - heavy white card with plain white or white and black or white and grey text.

The key logo image for the company is a question mark and I am open to suggestions and ideas on design.

I have attached a file that includes a couple of styles that have caught my eye and my thoughts on them. Hopefully they communicate what I'm looking for.
Updates

Thank you for all the great suggestions and designs.

I really appreciated the effort and creative energy you put into your designs. I have now closed the project after selecting a design and advising the successful designer of the card that I am happy with.

Regards

Target Market(s)

Organisations (CEO's and Boards), Governments, Legal professionals, Membership Associations and aspiring professionals.

Industry/Entity Type

Lawyer

Requirements
Must have
• The key logo element is a question mark (?) and this needs to be incorporated.

Embossed style - cut outs or other design ideas interest me too.

The attached file has a number of sample ideas and comments on each one that I like.
Should not have
• I like crisp, modern fonts (Myriads etc...) and do not like embellished fonts or Times etc...

```html
<!DOCTYPE html>
<html lang="en">
<head>
<meta charset="utf-8">
<title>The Kestrel Bureau – Business Card</title>
<link rel="stylesheet" href="https://fonts.googleapis.com/css2?family=Mulish:wght@400;600;800&display=swap">
<style>
  :root {
    --page: #ffffff;
    --card-edge: #000000;
    --front-bg: #ffffff;
    --panel: #ececec;
    --mark-ink: #2e2e2e;
    --mark-soft: #9a9a9a;
    --back-bg: #000000;
    --back-name: #8c8c8c;
    --back-title: #d6d6d6;
    --back-text: #c8c8c8;
    --back-faint: #3a3a3a;
  }
  * { margin: 0; padding: 0; box-sizing: border-box; }
  html, body {
    width: 1200px; height: 900px; overflow: hidden;
    background: var(--page);
    font-family: "Mulish", "Helvetica Neue", Arial, sans-serif;
  }
  .card {
    position: absolute; left: 70px; top: 166px;
    width: 1060px; height: 600px;
    border: 3px solid var(--card-edge);
    display: flex;
  }
  .card-front {
    position: relative; width: 534px; height: 100%;
    background: var(--front-bg);
  }
  .front-panel {
    position: absolute; left: 8px; top: 8px;
    width: 512px; height: 578px;
    border-radius: 36px;
    background: var(--panel);
  }
  .brand-mark {
    position: absolute; left: 0; right: 0; top: 170px; height: 220px;
    display: flex; align-items: center; justify-content: center; gap: 22px;
  }
  .brand-dot {
    width: 38px; height: 38px; border-radius: 50%;
    background: var(--mark-ink);
  }
  .brand-initials {
    font-weight: 800; font-size: 150px; letter-spacing: 4px;
    color: var(--mark-ink); line-height: 1;
  }
  .brand-name {
    position: absolute; left: 0; right: 0; top: 486px;
    text-align: center;
    font-weight: 600; font-size: 40px; color: var(--mark-soft);
  }
  .card-back {
    position: relative; flex: 1; height: 100%;
    background: var(--back-bg);
    color: var(--back-text);
  }
  .holder {
    position: absolute; left: 18px; top: 16px;
    font-size: 22px; color: var(--back-name);
  }
  .company {
    position: absolute; left: 12px; top: 222px;
  }
  .company-name {
    font-size: 31px; font-weight: 400; letter-spacing: 1px;
    color: var(--back-title);
  }
  .company-address {
    font-size: 18px; margin-top: 2px; color: var(--back-title);
  }
  .contact {
    position: absolute; left: 18px; top: 462px;
    list-style: none; font-size: 24px; line-height: 36px;
  }
  .back-initials {
    position: absolute; left: 300px; top: 340px;
    font-weight: 800; font-size: 96px; line-height: 1; color: var(--back-faint);
  }
</style>
</head>
<body>
  <div class="card">
    <section class="card-front">
      <div class="front-panel"></div>
      <div class="brand-mark">
        <span class="brand-dot"></span>
        <span class="brand-initials">KLB</span>
      </div>
      <div class="brand-name">The Kestrel Bureau</div>
    </section>
    <section class="card-back">
      <p class="holder">Dr. Mara Ellison, Director</p>
      <div class="company">
        <p class="company-name">THE KESTREL BUREAU</p>
        <p class="company-address">PO BOX 4417, HARLOW VALE, SYDNEY, AUSTRALIA</p>
      </div>
      <div class="back-initials">KLB</div>
      <ul class="contact">
        <li>M:::+61400 555 012</li>
        <li>P:::+612 9000 4471</li>
        <li>E:::mara@kestrelbureau.com.au</li>
      </ul>
    </section>
  </div>
</body>
</html>
```